Merchandising für Schülermarketing
Zielgruppe
FALDO Cash & Carry gibt es bereits seit 1964. Die FALDO Cash & Carry Deutschland GmbH zählt national und international zu den Marktführern im Großhandel und betreibt mit den Marken FALDO und V+V BRÜNDEL 107 Cash & Carry Märkte in Deutschland mit mehr als 17.000 Mitarbeitern. Wir haben 50.000 Artikel im Sortiment und bedienen damit Kunden aus Gastronomie, Hotellerie, Kiosken, Tankstellen, Vereinen, Freiberuflern, etc.
Für unsere Ausbildungsberufe in den Großmärkten (insbes. Kaufmann im Groß- und Außenhandel, Verkäufer, Einzelhandelskaufmann, Fachkraft für Lagerlogistik) suchen wir deutschlandweit viele Azubis. Zielgruppe sind Schüler mit mind. Realschulabschluss.
Aufgabenstellung
Deutschlandweit nehmen wir für das Azubimarketing auf verschiedenen Recruitingmessen teil. Dort verteilen wir Infomaterial aber auch Giveaways. Die Giveaways aktualisieren wir derzeit (Kulis, Textmarker in blau & gelb, faltbarer Einkaufsbeutel mit Logo). Neu dazu soll ein Jutebeutel für die Zielgruppe Schüler kommen, für den wir ein Design suchen.
Der Beutel soll das aktuelle Firmenlogo sichtbar tragen, aber dennoch optisch für die junge Zielgruppe ansprechend sein, so dass er regelmäßig genutzt wird. Gern kann das Design einen grafischen Aufdruck beinhalten oder einen witzigen Spruch, der irgendwie mit Arbeiten bei Faldo in Zusammenhang steht.

```html
<!DOCTYPE html>
<html lang="de">
<head>
<meta charset="utf-8">
<title>Zeugnis – Jutebeutel Schülermarketing</title>
<link href="https://fonts.googleapis.com/css2?family=Inter:wght@400;700;900&family=Shadows+Into+Light&display=swap" rel="stylesheet">
<style>
  :root{
    --ink:#1a1a1a;
    --paper:#ffffff;
    --stage:#ececec;
    --pen:#1d5fb4;
    --leader:#9a9a9a;
    --brand-navy:#0b2a78;
    --smiley:#f6c424;
    --smiley-edge:#e29a12;
    --poo:#7a4a1f;
  }
  *{margin:0;padding:0;box-sizing:border-box}
  html,body{width:1200px;height:776px;overflow:hidden;background:var(--stage)}
  body{font-family:"Inter",Arial,sans-serif;color:var(--ink)}
  .sheet{position:absolute;left:267px;top:0;width:665px;height:776px;background:var(--paper)}
  .title{position:absolute;left:131px;top:38px;width:394px;text-align:center;font-weight:900;font-size:88px;letter-spacing:-1px;line-height:1}
  .title-rule{position:absolute;left:131px;top:127px;width:394px;border-top:1.5px solid var(--ink)}
  .school-year{position:absolute;left:131px;top:136px;width:394px;text-align:center;font-size:16px}
  .field-label{position:absolute;font-size:13px;line-height:1}
  .field-line{position:absolute;border-bottom:1px solid var(--ink);height:1px}
  .handwriting{position:absolute;font-family:"Shadows Into Light",cursive;color:var(--pen);line-height:1;white-space:nowrap}
  .row{position:absolute;height:16px;display:flex;align-items:flex-end}
  .row .label{font-size:13px;line-height:1;white-space:nowrap;padding-right:6px}
  .row.subject .label{font-weight:700}
  .row .leader{flex:1;border-bottom:1px dotted var(--leader);margin-bottom:2px}
  .write-row{position:absolute;height:16px;display:flex;align-items:flex-end}
  .write-row .blank{width:114px;border-bottom:1px solid var(--ink);margin-right:6px;position:relative}
  .write-row .blank .handwriting{left:6px;bottom:2px;font-size:26px}
  .write-row .leader{flex:1;border-bottom:1px dotted var(--leader);margin-bottom:0}
  .mark{position:absolute;width:35px;height:35px;border-radius:50%;background:radial-gradient(circle at 40% 35%,#ffe36a,var(--smiley) 55%,var(--smiley-edge))}
  .mark.poo{border-radius:50% 50% 45% 45%;background:radial-gradient(circle at 45% 35%,#a26a34,var(--poo))}
  .remark-label{position:absolute;left:39px;top:714px;font-size:13px}
  .remark{position:absolute;left:122px;top:698px;display:flex;align-items:flex-end;gap:10px;font-weight:700;font-size:13px}
  .brand-name{font-weight:700;font-size:30px;line-height:1;color:var(--brand-navy);margin:0 6px}
  .remark-rule{position:absolute;left:117px;top:726px;width:500px;border-top:1px solid var(--ink)}
  .web{position:absolute;left:122px;top:730px;font-weight:700;font-size:13px;color:var(--brand-navy)}
</style>
</head>
<body>
<main class="sheet">
  <h1 class="title">ZEUGNIS</h1>
  <div class="title-rule"></div>
  <p class="school-year">Schuljahr 2017/2018</p>

  <span class="field-label" style="left:39px;top:205px">für</span>
  <div class="field-line" style="left:62px;top:216px;width:344px"></div>
  <span class="handwriting" style="left:76px;top:188px;font-size:28px">Max Mustermann</span>
  <span class="field-label" style="left:432px;top:205px">Klasse</span>
  <div class="field-line" style="left:479px;top:216px;width:138px"></div>
  <span class="handwriting" style="left:540px;top:188px;font-size:28px">8c</span>

  <!-- Kopfnoten -->
  <div class="row" style="left:39px;top:264px;width:224px"><span class="label">Benehmen</span><span class="leader"></span></div>
  <div class="mark" style="left:269px;top:255px" role="img" aria-label="Smiley mit Sonnenbrille"></div>
  <div class="row" style="left:39px;top:307px;width:224px"><span class="label">Fleiß</span><span class="leader"></span></div>
  <div class="mark" style="left:269px;top:298px" role="img" aria-label="Smiley mit Brille"></div>

  <div class="row" style="left:355px;top:264px;width:222px"><span class="label">Mitarbeit</span><span class="leader"></span></div>
  <div class="mark" style="left:586px;top:248px" role="img" aria-label="Smiley mit Heiligenschein"></div>
  <div class="write-row" style="left:355px;top:305px;width:222px"><span class="blank"><span class="handwriting">Ordnung</span></span><span class="leader"></span></div>
  <div class="mark" style="left:586px;top:298px" role="img" aria-label="Weinender Smiley"></div>

  <!-- Fächer links -->
  <div class="row subject" style="left:39px;top:391px;width:224px"><span class="label">Deutsch</span><span class="leader"></span></div>
  <div class="mark" style="left:269px;top:379px" role="img" aria-label="Grinsender Smiley"></div>
  <div class="row subject" style="left:39px;top:435px;width:224px"><span class="label">Englisch</span><span class="leader"></span></div>
  <div class="mark" style="left:269px;top:423px" role="img" aria-label="Zwinkernder Smiley mit Zunge"></div>
  <div class="row subject" style="left:39px;top:478px;width:224px"><span class="label">Mathematik</span><span class="leader"></span></div>
  <div class="mark" style="left:269px;top:467px" role="img" aria-label="Smiley mit Sonnenbrille"></div>
  <div class="write-row" style="left:39px;top:522px;width:224px"><span class="blank"><span class="handwriting">Französisch</span></span><span class="leader"></span></div>
  <div class="mark" style="left:269px;top:510px" role="img" aria-label="Verwirrter Smiley"></div>
  <div class="write-row" style="left:39px;top:565px;width:224px"><span class="blank"><span class="handwriting">Latein</span></span><span class="leader"></span></div>
  <div class="mark poo" style="left:269px;top:553px" role="img" aria-label="Haufen-Emoji"></div>
  <div class="row subject" style="left:39px;top:611px;width:224px"><span class="label">Kunst</span><span class="leader"></span></div>
  <div class="mark" style="left:269px;top:598px" role="img" aria-label="Smiley mit Augenbinde"></div>

  <!-- Fächer rechts -->
  <div class="row subject" style="left:355px;top:391px;width:222px"><span class="label">Physik</span><span class="leader"></span></div>
  <div class="mark" style="left:586px;top:379px" role="img" aria-label="Schreiender Smiley"></div>
  <div class="write-row" style="left:355px;top:434px;width:222px"><span class="blank"><span class="handwriting">Chemie</span></span><span class="leader"></span></div>
  <div class="mark" style="left:586px;top:423px" role="img" aria-label="Lachender Smiley"></div>
  <div class="write-row" style="left:355px;top:478px;width:222px"><span class="blank"><span class="handwriting">Musik</span></span><span class="leader"></span></div>
  <div class="mark poo" style="left:586px;top:469px" role="img" aria-label="Haufen-Emoji"></div>
  <div class="row subject" style="left:355px;top:522px;width:222px"><span class="label">Erdkunde</span><span class="leader"></span></div>
  <div class="mark" style="left:586px;top:512px" role="img" aria-label="Smiley mit Reißverschlussmund"></div>
  <div class="row subject" style="left:355px;top:566px;width:222px"><span class="label">Sport</span><span class="leader"></span></div>
  <div class="mark" style="left:586px;top:555px" role="img" aria-label="Smiley mit Sonnenbrille"></div>
  <div class="write-row" style="left:355px;top:609px;width:222px"><span class="blank"><span class="handwriting">Ethik</span></span><span class="leader"></span></div>
  <div class="mark" style="left:586px;top:598px" role="img" aria-label="Verliebter Smiley"></div>

  <!-- Anmerkung -->
  <span class="remark-label">Anmerkung:</span>
  <p class="remark"><span>Schüler/-in kann eine große Zukunft bei</span><span class="brand-name">FALDO</span><span>erwarten.</span></p>
  <div class="remark-rule"></div>
  <a class="web">www.faldo-beispiel.de</a>
</main>
</body>
</html>
```